Website Design for a different kind of Business Consulting organisation needed!

We need a website design that reflects who we are, the simplicity of our consulting business and with a focus on our priority - to help our clients deliver, or execute - the "e" in Vantor-a.

Our key high level requirements are:
1) Simple and intuitive look and feel
2) Integration with all key social media platforms, chirpnet, pagebook, workring, scrollo.

10 pages, tops.
- Main page - Welcome
- About Us/ Who are Vantor-a?
- 5 services pages - Project Management, Business Process Management, Change Management, Business Analysis and Finance Systems
- Contact Us

Something like:
http://www.lmvholdings.example/

Vantor-a is a registered trademark and all Logos and other branded material are attached for reference.

So, what’s our gig: A few snippets from previous work...

We are a different kind of business consulting group. We partner with our clients to help them deliver change. We don't just provide them with the theory. We also provide them with the leadership and capability to execute the change.

We aren’t a one stop shop, and we don’t offer cookie cutter solutions. We’re a boutique consulting firm covering Project Management, Business Process Management, Change Management and Business Analytics.

Vantor-a is a professional services organisation that partners with their clients to lead the execution of strategic process and system improvement initiatives. Vantor-a combines hands on delivery with coaching in best practice methodologies and approaches to build their clients capabilities to ensure their ongoing success in project implementations.

UPDATES:

Thanks to everyone who has submitted designs so far. The standard of designs coming through is quite high, with lots of professional designs that nail the design brief. Eliminating them is proving to be quite challenging.

A few updates to the job brief:
- Please make sure the design fits on one page. We would like all of our information to be on the first page that people see without them having to scroll down
- Please ensure you include the FIVE services we offer in the design
- Please use corporate images/snapvault photos in your designs which are relevant to our business
- Please add a section for a live chirpnet feed from our chirpnet account and a link to plaza+
- Please add a section for news/updates

Also, if you are able to build a site once a design is selected, please let us know.

Thanks,

Marcela.

Target Market(s)

Our target customers are large enterprises in Australia that are growing rapidly and have recently (last 24 months) undertaken or are currently undergoing software implementations and business process improvement programs. These businesses have a turnover of $100m or above and are working hard to differentiate themselves from their competitors but are not seeing the return on investment promised by software vendors and process improvement initiatives.

Industry/Entity Type

Leadership

Requirements
Must have
• Collaboration / Training / Workshop / Consulting images all of a professional nature.
Simple, non-cluttered look with plenty of white space.

```html
<!DOCTYPE html>
<html lang="en">
<head>
<meta charset="utf-8">
<title>Vantor-a Consulting</title>
<link href="https://fonts.googleapis.com/css2?family=PT+Sans:wght@400;700&display=swap" rel="stylesheet">
<style>
  :root {
    --brand-blue: #0d4a9a;
    --deep-blue: #0a3c86;
    --link-blue: #1d97d5;
    --nav-ink: #222222;
    --body-ink: #5a5a5a;
    --head-ink: #222222;
    --panel-bg: #f1f1f1;
    --rule: #d8d8d8;
    --footer-blue: #0b4a9c;
    --footer-link: #d7e6f7;
    --footer-soft: #57a9ef;
    --orange: #f47b16;
    --sky: #3aa3d6;
    --green: #3fae49;
    --amber: #f6b40e;
    --teal: #0f8f83;
    --tweet-green: #3a9a3a;
  }
  * { box-sizing: border-box; margin: 0; padding: 0; }
  html, body { width: 1200px; height: 740px; overflow: hidden; background: #fff; }
  body { font-family: "PT Sans", Arial, sans-serif; color: var(--body-ink); }
  .stage { position: relative; width: 1200px; height: 740px; overflow: hidden; }

  .top-strip { position: absolute; top: 0; left: 0; width: 1200px; height: 8px;
    background: linear-gradient(#dcdcdc, #f4f4f4); }
  .site-header { position: absolute; top: 8px; left: 0; width: 1200px; height: 62px; }
  .brand { position: absolute; left: 257px; top: 16px; display: flex; align-items: center; gap: 6px;
    font-size: 28px; font-weight: 400; color: var(--brand-blue); letter-spacing: 0.5px; }
  .brand-dot { width: 12px; height: 12px; border-radius: 50%; background: var(--brand-blue); }
  .main-nav { position: absolute; left: 629px; top: 28px; display: flex; gap: 24px;
    font-size: 11px; font-weight: 700; color: var(--nav-ink); text-transform: uppercase; }
  .main-nav .is-current { color: var(--brand-blue); }

  .hero { position: absolute; top: 70px; left: 0; width: 1200px; height: 300px;
    background: linear-gradient(100deg, #0a3a84 0%, #1452a8 45%, #1a5cb3 70%, #1550a4 100%); overflow: hidden; }
  .hero-shape { position: absolute; background: rgba(255,255,255,0.05); }
  .hero-shape.a { left: 140px; top: 40px; width: 260px; height: 320px; transform: skewX(-14deg); }
  .hero-shape.b { left: 560px; top: 0; width: 180px; height: 300px; transform: skewX(-10deg); background: rgba(0,0,0,0.06); }
  .hero-portrait { position: absolute; left: 600px; top: 0; width: 360px; height: 300px;
    background: radial-gradient(ellipse at 55% 55%, #c9a58a 0%, #7c8fa8 40%, rgba(26,92,179,0) 75%); }
  .hero-copy { position: absolute; left: 275px; top: 73px; width: 360px; color: #fff; }
  .hero-copy h1 { font-size: 28px; line-height: 31px; font-weight: 700; }
  .hero-copy p { margin-top: 12px; font-family: Arial, Helvetica, sans-serif; font-size: 10px; color: #dfe8f5; }

  .hero-fade { position: absolute; top: 370px; left: 0; width: 1200px; height: 22px;
    background: linear-gradient(#dedede, #ffffff); }

  .services { position: absolute; left: 253px; top: 325px; width: 692px; height: 127px;
    background: var(--panel-bg); border-radius: 4px; box-shadow: 0 1px 4px rgba(0,0,0,0.3);
    display: grid; grid-template-columns: 143px 132px 140px 136px 141px; }
  .service { position: relative; padding: 11px 8px 0 17px; }
  .service + .service { box-shadow: inset 1px 0 0 #e2e2e2, inset 2px 0 0 #fafafa; }
  .service-icon { width: 38px; height: 38px; border-radius: 50%; margin-left: 30px;
    border: 2px solid #fff; box-shadow: 0 0 0 1px rgba(0,0,0,0.12); display: flex; align-items: center; justify-content: center; }
  .service-icon.orange { background: var(--orange); }
  .service-icon.sky { background: var(--sky); }
  .service-icon.green { background: var(--green); }
  .service-icon.amber { background: var(--amber); }
  .service-icon.teal { background: var(--teal); }
  .service h3 { margin-top: 10px; font-size: 12px; line-height: 14px; font-weight: 700; color: var(--head-ink); }
  .service p { margin-top: 4px; font-size: 7.5px; line-height: 11px; color: #666; }

  .news { position: absolute; left: 271px; top: 474px; width: 446px; }
  .section-head { display: flex; justify-content: space-between; align-items: center;
    padding-bottom: 4px; border-bottom: 1px solid var(--rule); }
  .section-head h2 { font-size: 14px; font-weight: 700; color: var(--brand-blue); }
  .arrow-dot { width: 12px; height: 12px; border-radius: 50%; background: #d0d0d0; display: flex; align-items: center; justify-content: center; }
  .date-badge { position: absolute; left: -1px; top: 37px; width: 51px; height: 38px; background: var(--brand-blue);
    color: #fff; text-align: center; }
  .date-badge .day { font-size: 20px; line-height: 22px; }
  .date-badge .month { font-size: 7.5px; }
  .news-photo { position: absolute; left: 61px; top: 36px; width: 193px; height: 113px;
    background: linear-gradient(120deg, #6c6f75, #b7b2ab 50%, #8a8c92); }
  .news-body { position: absolute; left: 269px; top: 27px; width: 180px; }
  .news-body h3 { font-size: 12.5px; line-height: 17px; font-weight: 700; color: var(--head-ink); }
  .news-body p { margin-top: 8px; font-size: 8px; line-height: 14px; color: #666; }
  .read-more { display: inline-block; margin-top: 5px; font-size: 8px; color: var(--brand-blue); text-decoration: none; }

  .chirps { position: absolute; left: 757px; top: 474px; width: 185px; }
  .follow-btn { display: flex; align-items: center; gap: 4px; padding: 1px 5px; font-size: 9px; color: #2b4a6a;
    background: linear-gradient(#f8fbfe, #d9e7f3); border: 1px solid #a9c3da; border-radius: 2px; }
  .follow-btn span.dot { width: 8px; height: 8px; border-radius: 50%; background: var(--link-blue); }
  .chirps .section-head { border-bottom-color: var(--rule); }
  .chirp-list { position: relative; margin-top: 8px; padding-right: 8px; height: 154px; border-right: 3px solid #e6e6e6; }
  .chirp-list::after { content: ""; position: absolute; right: -3px; top: 12px; width: 3px; height: 21px; background: var(--link-blue); }
  .chirp { margin: 0 0 10px 0; font-size: 9px; line-height: 12px; color: #555; }
  .chirp a { color: var(--link-blue); text-decoration: none; }
  .chirp time { display: block; font-size: 7.5px; color: #444; }
  .chirp-follow { margin-top: 4px; padding-top: 6px; border-top: 1px solid #e4e4e4; font-size: 9px; color: #555; padding-left: 2px; }
  .chirp-follow a { color: var(--tweet-green); text-decoration: none; }

  .site-footer { position: absolute; left: 0; top: 694px; width: 1200px; height: 46px; background: var(--footer-blue); }
  .footer-nav { position: absolute; left: 258px; top: 9px; display: flex; gap: 0; font-size: 8.5px; color: var(--footer-link); }
  .footer-nav a { color: var(--footer-link); text-decoration: none; }
  .footer-nav .sep { margin: 0 9px; }
  .copyright { position: absolute; left: 259px; top: 25px; font-size: 8.5px; color: var(--footer-soft); }
  .social { position: absolute; left: 780px; top: 13px; display: flex; gap: 10px; }
  .social a { display: flex; align-items: center; gap: 3px; font-size: 8px; color: #fff; text-decoration: none; }
  .social .ring { width: 10px; height: 10px; border-radius: 50%; border: 1px solid #cfe0f3; }
  .social .ring.active { background: var(--link-blue); border-color: var(--link-blue); }
</style>
</head>
<body>
<div class="stage">
  <div class="top-strip"></div>

  <header class="site-header">
    <div class="brand"><span>Vantor-a</span><span class="brand-dot"></span></div>
    <nav class="main-nav">
      <span class="is-current">Home</span>
      <span>Who are Vantor-a?</span>
      <span>Our Services</span>
      <span>Contact Us</span>
    </nav>
  </header>

  <section class="hero">
    <div class="hero-shape a"></div>
    <div class="hero-shape b"></div>
    <div class="hero-portrait" role="img" aria-label="Smiling businesswoman in a dark blazer, office background"></div>
    <div class="hero-copy">
      <h1>Vantor-a Consultants are invaluable to the success of my business</h1>
      <p>Help me to boost my self-confidence at every stage</p>
    </div>
  </section>
  <div class="hero-fade"></div>

  <section class="services">
    <article class="service">
      <div class="service-icon orange">
        <svg width="18" height="18" viewBox="0 0 18 18" fill="none" stroke="#fff" stroke-width="1.8"><rect x="2" y="3" width="14" height="9" rx="1"/><path d="M9 12v3M5.5 15.5h7"/></svg>
      </div>
      <h3>Project Management</h3>
      <p>Maecenas id mi ante. Morbi scing molestie convallis. Morbi est laliquam ut arcu.</p>
    </article>
    <article class="service">
      <div class="service-icon sky">
        <svg width="18" height="18" viewBox="0 0 18 18" fill="#fff"><rect x="2" y="5.5" width="14" height="9" rx="1"/><path d="M6.5 5.5V3.5h5v2" fill="none" stroke="#fff" stroke-width="1.5"/></svg>
      </div>
      <h3>Business Process Management</h3>
      <p>Maecenas id mi ante. Morbi adipiscing molestie convallis.</p>
    </article>
    <article class="service">
      <div class="service-icon green">
        <svg width="18" height="18" viewBox="0 0 18 18" fill="none" stroke="#fff" stroke-width="1.6"><rect x="2.5" y="2.5" width="13" height="13"/><path d="M5.5 9l2.5 2.5 4.5-5"/></svg>
      </div>
      <h3>Change Management</h3>
      <p>Maecenas id mi ante. Morbi scing molestie convallis. Morbi est laliquam ut arcu.</p>
    </article>
    <article class="service">
      <div class="service-icon amber">
        <svg width="20" height="18" viewBox="0 0 20 18" fill="none" stroke="#fff" stroke-width="1.6"><path d="M1.5 9C4 5 7 3.5 10 3.5S16 5 18.5 9C16 13 13 14.5 10 14.5S4 13 1.5 9z"/><circle cx="10" cy="9" r="2.6" fill="#fff"/></svg>
      </div>
      <h3>Business Analysis</h3>
      <p>Maecenas id mi ante. Morbi scing molestie convallis. Morbi est laliquam ut arcu.</p>
    </article>
    <article class="service">
      <div class="service-icon teal">
        <svg width="16" height="18" viewBox="0 0 16 18" fill="#fff"><rect x="2" y="1" width="12" height="16" rx="1"/><rect x="4" y="3" width="8" height="3" fill="#0f8f83"/><g fill="#0f8f83"><rect x="4" y="8" width="2" height="2"/><rect x="7" y="8" width="2" height="2"/><rect x="10" y="8" width="2" height="2"/><rect x="4" y="11" width="2" height="2"/><rect x="7" y="11" width="2" height="2"/><rect x="10" y="11" width="2" height="2"/><rect x="4" y="14" width="2" height="2"/><rect x="7" y="14" width="2" height="2"/><rect x="10" y="14" width="2" height="2"/></g></svg>
      </div>
      <h3>Finance Systems</h3>
      <p>Maecenas id mi ante. Morbi scing molestie convallis. Morbi est laliquam ut arcu.</p>
    </article>
  </section>

  <section class="news">
    <div class="section-head">
      <h2>Latest News &amp; Updates</h2>
      <span class="arrow-dot"><svg width="6" height="6" viewBox="0 0 6 6"><path d="M2 1l2 2-2 2" fill="none" stroke="#fff" stroke-width="1.2"/></svg></span>
    </div>
    <div class="date-badge"><div class="day">25</div><div class="month">March, 2014</div></div>
    <div class="news-photo" role="img" aria-label="Smiling senior businessman in front of his team"></div>
    <div class="news-body">
      <h3>Lorem Ipsums Un Voluptas Sadips Nemis Fugiat Dolores</h3>
      <p>At vero eos et accusamus et iusto odios un dignissimos ducimus qui blan ditiis praxiser esentium voluptatum un deleniti atqueste sites excep turiitate non providentsim ...</p>
      <a class="read-more" href="#">Read More &nbsp;›</a>
    </div>
  </section>

  <aside class="chirps">
    <div class="section-head">
      <h2>Chirps</h2>
      <span class="follow-btn"><span class="dot"></span>Follow</span>
    </div>
    <div class="chirp-list">
      <p class="chirp">Experience more with expanded Chirps<br><a href="#">http://cn.example/8gH7sqUE</a><time>18 hours ago</time></p>
      <p class="chirp">Tailored Trends bring you closer<br><a href="#">http://cn.example/ppv0hqF2</a><time>03 Nov 2012</time></p>
      <p class="chirp">Our new nest. <a href="#">http://cn.example/6Ugo6xbA</a><time>28 Oct 2012</time></p>
      <p class="chirp-follow">Follow me <a href="#">@vantor-a.au</a></p>
    </div>
  </aside>

  <footer class="site-footer">
    <nav class="footer-nav">
      <a href="#">Home</a><span class="sep">|</span>
      <a href="#">About Us</a><span class="sep">|</span>
      <a href="#">Our Services</a><span class="sep">|</span>
      <a href="#">Contact us</a><span class="sep">|</span>
      <a href="#">Terms</a><span class="sep">|</span>
      <a href="#">Latatest News</a>
    </nav>
    <p class="copyright">© Copyright &nbsp;www.vantor-a.example . All Rights Reserved</p>
    <div class="social">
      <a href="#"><span class="ring"></span>pagebook</a>
      <a href="#"><span class="ring active"></span>chirpnet</a>
      <a href="#"><span class="ring"></span>feed</a>
      <a href="#"><span class="ring"></span>plaza+</a>
    </div>
  </footer>
</div>
</body>
</html>
```